Need A Fresher Look & Feel For Our Water Testing Product

We need one insert design for our at home water testing, we're looking something that pops a bit more than we currently have.

We're looking to show that it's an at-home test that allows you to test for multiple things with one easy to use test. Also the fact it includes double tests for almost everything (except bacteria).
Updates

Low design quality

Target Market(s)

Men and women aged 30-60

Industry/Entity Type

Water Company

Font styles to use
Serif

Colors
33a6d7
85cae6

Requirements
Must have
• This packaging will be a little bit different dimensions, we are going to be using a zippered pouch that has a matte finish. Here's an example of the type of packaging. https://im07.verpogrix.com/kf/QRM4k72nbuXP5TqLWdve8GZRRMsk/Laminated-aluminum-foil-zip-lock-bag-stand.jpg_350x350.jpg
• The dimensions of our pouch will be: 5.75in x 5.5in
• Looking for something clean that really pops, try to use blues because of the water testing aspect. We like to use clean crisp light colors to signify cleanliness and clean water.
• We want some kind of color wheel like we currently have that gives a different color for each of the following tests. It helps make it pop out seeing that 8 different types of tests are included.
• - E. Coli / Bacteria
• - pH
• - Total Alkalinity
• - Total Hardness
• - Total Chlorine
• - Nitrite
• - Nitrate
• - Heavy Metals
• Also maybe make a point the kit includes 2 tests for each of the following: (Only one without 3 is the bacteria)
• - pH
• - Total Alkalinity
• - Total Hardness
• - Total Chlorine
• - Nitritie
• - Nirtate
• - Heavy Metals
• IMPORTANT!
• The blue & white below should be the main colors, but you please choose the 8 colors for the color wheel.
Nice to have
• We have another similar older kit which the packaging is attached for. We want the new one to be much more eye catching the current one.

```html
<!DOCTYPE html>
<html lang="en">
<head>
<meta charset="UTF-8">
<title>The Complete Water Analysis Test Kit – Pouch Insert</title>
<link href="https://fonts.googleapis.com/css2?family=Alegreya:ital,wght@0,400;0,700;1,400&display=swap" rel="stylesheet">
<style>
  :root {
    --brand-blue: #33a6d7;
    --brand-light: #85cae6;
    --deep-blue: #1a7fc4;
    --ink: #555a5e;
    --backdrop: #a9a9a9;
    --paper: #ffffff;
    --badge-red: #d4202e;
    --pill-bacteria: #6cc17a;
    --pill-chlorine: #45c1a8;
    --pill-ph: #f0a02c;
    --pill-nitrite: #2ea7e0;
    --pill-alkalinity: #5ec5d6;
    --pill-nitrate: #da2f4b;
    --pill-hardness: #d982b8;
    --pill-metals: #7d7776;
  }
  * { box-sizing: border-box; margin: 0; padding: 0; }
  html, body {
    width: 1200px; height: 779px; overflow: hidden;
    background: var(--backdrop);
    font-family: "Alegreya", Georgia, serif;
  }
  .insert {
    position: absolute; left: 210px; top: 17px;
    width: 780px; height: 745px;
    background: var(--paper);
    box-shadow: 0 4px 10px rgba(0,0,0,0.25);
    overflow: hidden;
  }
  .splash-art {
    position: absolute; left: 400px; top: 80px;
    width: 370px; height: 490px;
    border-radius: 45% 55% 40% 60% / 50% 45% 55% 50%;
    background: radial-gradient(circle at 45% 60%, #e6f4fb 0%, var(--brand-light) 45%, var(--brand-blue) 75%, var(--deep-blue) 100%);
    opacity: 0.9;
  }
  .title {
    position: absolute; left: 46px; top: 20px;
    color: var(--brand-blue);
    font-weight: 400; font-size: 51px; line-height: 68px;
    letter-spacing: 0.5px;
  }
  .subtitle {
    position: absolute; left: 46px; top: 224px;
    color: var(--ink); font-style: italic;
    font-size: 30px; line-height: 41px;
  }
  .contents-heading {
    position: absolute; left: 46px; top: 318px;
    color: var(--ink); font-weight: 700; font-size: 19px;
  }
  .test-list {
    position: absolute; left: 40px; top: 353px;
    display: grid; grid-template-columns: 157px 157px;
    column-gap: 5px; row-gap: 7px; list-style: none;
  }
  .test-pill {
    height: 23px; border-radius: 12px;
    color: #fff; font-size: 17px; line-height: 23px;
    padding-left: 7px; white-space: nowrap;
  }
  .test-pill::before { content: "• "; }
  .pill-bacteria { background: var(--pill-bacteria); }
  .pill-chlorine { background: var(--pill-chlorine); }
  .pill-ph { background: var(--pill-ph); }
  .pill-nitrite { background: var(--pill-nitrite); }
  .pill-alkalinity { background: var(--pill-alkalinity); }
  .pill-nitrate { background: var(--pill-nitrate); }
  .pill-hardness { background: var(--pill-hardness); }
  .pill-metals { background: var(--pill-metals); }
  .tagline-curve {
    position: absolute; left: 0; top: 0;
  }
  .tagline-curve text {
    fill: var(--ink); font-family: "Alegreya", Georgia, serif;
    font-style: italic; font-size: 22px;
  }
  .badge {
    position: absolute; left: 610px; top: 574px;
    width: 148px; height: 148px; border-radius: 50%;
    background: var(--badge-red); color: #fff;
    text-align: center; padding-top: 32px;
  }
  .badge-line { display: block; font-size: 15px; line-height: 19px; }
  .badge-strong { font-weight: 700; font-size: 17px; }
  .badge-big { font-weight: 700; font-size: 24px; line-height: 28px; }
  .brand {
    position: absolute; left: 41px; top: 654px;
  }
  .brand-name {
    display: block; color: var(--brand-blue);
    font-size: 40px; font-weight: 700; line-height: 42px;
    letter-spacing: 1px;
  }
  .brand-tagline {
    display: block; color: var(--brand-blue);
    font-size: 9.5px; letter-spacing: 3.6px; margin-top: 2px;
  }
  .origin {
    position: absolute; left: 315px; top: 656px; text-align: center;
  }
  .flag {
    width: 68px; height: 44px;
    background: linear-gradient(135deg, #2a3f8f 0 35%, #d9262e 35% 100%);
  }
  .origin-label {
    display: block; color: #2a3f8f; font-size: 10px; font-weight: 700;
    margin-top: 4px; font-family: Arial, sans-serif;
  }
</style>
</head>
<body>
  <main class="insert">
    <div class="splash-art" role="img" aria-label="Blue water splash with droplets and a sweeping wave"></div>

    <h1 class="title">THE COMPLETE<br>WATER ANALYSIS<br>TEST KIT</h1>
    <p class="subtitle">Easy at-home testing kit for<br>both well &amp; municipal water</p>

    <h2 class="contents-heading">Test kit contains the following:</h2>
    <ul class="test-list">
      <li class="test-pill pill-bacteria">E. Coli / Bacteria</li>
      <li class="test-pill pill-chlorine">Total Chlorine *</li>
      <li class="test-pill pill-ph">pH *</li>
      <li class="test-pill pill-nitrite">Nitrite *</li>
      <li class="test-pill pill-alkalinity">Total Alkalinity *</li>
      <li class="test-pill pill-nitrate">Nitrate *</li>
      <li class="test-pill pill-hardness">Total Hardness *</li>
      <li class="test-pill pill-metals">Heavy Metals *</li>
    </ul>

    <svg class="tagline-curve" width="780" height="745" viewBox="0 0 780 745">
      <defs>
        <path id="tagline-path" d="M 250 578 Q 470 635 660 540" fill="none"/>
      </defs>
      <text><textPath href="#tagline-path">Know what you and your family are drinking</textPath></text>
    </svg>

    <div class="badge">
      <span class="badge-line badge-strong">*TEST KIT</span>
      <span class="badge-line">INCLUDES</span>
      <span class="badge-line badge-big">2 TESTS</span>
      <span class="badge-line">FOR EACH</span>
    </div>

    <div class="brand">
      <span class="brand-name">AQUAVERITY</span>
      <span class="brand-tagline">WATER TESTING KITS &amp; SUPPLIES</span>
    </div>

    <div class="origin">
      <div class="flag" role="img" aria-label="Waving national flag"></div>
      <span class="origin-label">MADE IN USA</span>
    </div>
  </main>
</body>
</html>
```